Tarvel Ridge LLC

Need Professional Business cards for New Investment Fund

Target Market(s)

High Quality investors

Industry/Entity Type

Financial

Contact Information for Business Card

Phone Number +1 555 284 6193
Name Pavel Orlinsky
Title Fund Manager
email po@FundTarvel.example
Website www.FundTarvel.example

Colors

Designer to choose colors to be used in the design.

Requirements
Must have
• Must have our Logo and all of the above. Must be made so lettering and loge can be raised

```html
<!DOCTYPE html>
<html lang="en">
<head>
<meta charset="utf-8">
<title>Tarvel Ridge LLC — Business Card</title>
<link rel="stylesheet" href="https://fonts.googleapis.com/css2?family=Jost:wght@400;500&display=swap">
<style>
  :root {
    --green: #58b947;
    --forest: #434f43;
    --ink: #111111;
    --muted: #8a8f95;
    --stone: #b3b3ad;
    --paper: #ffffff;
    --backdrop: #f1f2f4;
  }
  * { box-sizing: border-box; margin: 0; padding: 0; }
  html, body { width: 1200px; height: 1200px; overflow: hidden; }
  body {
    background: var(--backdrop);
    font-family: "Jost", "Futura", sans-serif;
    position: relative;
  }
  .card {
    position: absolute;
    left: 206px;
    width: 788px;
    height: 450px;
    overflow: hidden;
  }
  .card--front { top: 112px; background: var(--paper); }
  .card--back { top: 637px; background: var(--forest); }

  .holder-name {
    position: absolute; left: 97px; top: 141px;
    font-size: 29px; font-weight: 500; color: var(--ink);
    letter-spacing: 0.3px; line-height: 1.2;
  }
  .holder-title {
    position: absolute; left: 97px; top: 178px;
    font-size: 21px; font-weight: 400; color: var(--muted);
    letter-spacing: 0.4px; line-height: 1.2;
  }
  .contact {
    position: absolute; left: 97px;
    display: flex; align-items: center; gap: 14px;
    font-size: 24px; color: var(--muted); letter-spacing: 2.4px;
    line-height: 1.2; white-space: nowrap;
  }
  .contact--phone { top: 237px; }
  .contact--email { top: 279px; font-size: 23px; letter-spacing: 1.4px; gap: 12px; }
  .contact svg { flex: none; }

  .brand {
    display: flex; align-items: center; gap: 12px;
    font-weight: 500; white-space: nowrap; line-height: 1.2;
  }
  .brand__square { width: 20px; height: 20px; background: var(--green); flex: none; }
  .brand--front {
    position: absolute; left: 478px; top: 205px;
    font-size: 34px; color: var(--forest);
  }

  .band { position: absolute; left: 0; bottom: 0; height: 21px; }
  .band--green { width: 394px; background: var(--green); }
  .band--dark { left: 394px; right: 0; width: auto; background: var(--forest); }

  .back-lockup {
    position: absolute; left: 108px; top: 229px;
    transform: translateY(-50%);
    display: flex; align-items: center; gap: 26px;
  }
  .brand--back { font-size: 24px; color: var(--green); }
  .website {
    font-size: 30px; color: var(--stone); letter-spacing: 2px;
    line-height: 1.2; white-space: nowrap;
  }
</style>
</head>
<body>
  <section class="card card--front">
    <p class="holder-name">Pavel Orlinsky</p>
    <p class="holder-title">Title Fund Manager</p>
    <p class="contact contact--phone">
      <svg width="14" height="24" viewBox="0 0 14 24" aria-hidden="true"><path d="M10 1 C4 2 2 7 2 12 C2 17 4 22 10 23 L12 18 L9 17 C7 15 7 9 9 7 L12 6 Z" fill="var(--green)"/></svg>
      <span>+1 555 284 6193</span>
    </p>
    <p class="contact contact--email">
      <svg width="26" height="18" viewBox="0 0 26 18" aria-hidden="true"><rect x="0" y="0" width="26" height="18" fill="var(--green)"/><path d="M1 1 L13 10 L25 1 M1 17 L10 8 M25 17 L16 8" stroke="#fff" stroke-width="2" fill="none"/></svg>
      <span>po@FundTarvel.example</span>
    </p>
    <div class="brand brand--front">
      <span class="brand__square"></span>
      <span class="brand__name">Tarvel Ridge</span>
    </div>
    <div class="band band--green"></div>
    <div class="band band--dark"></div>
  </section>

  <section class="card card--back">
    <div class="back-lockup">
      <div class="brand brand--back">
        <span class="brand__name">Tarvel Ridge</span>
      </div>
      <p class="website">www.FundTarvel.example</p>
    </div>
  </section>
</body>
</html>
```